sydney wedding photography business needs a business card design

we need a business card design for a sydney based wedding photography and videography business. our business name is :golden hour photography and video. our target clients are 24-35 yrs female. our style is candid, organic, natural, dynamic. we are a team of young photographers and videographers, and help brides to create memories that they will cherish for the rest of their lives. the logo will be provided. we want an elegant design that reflects our style, and also want to give a great impression to our clients that we are one of the best studios in sydney and our brand means quality and premium service.

Target Market(s)

bride to be, 24-35 years old, living in sydney and surrunding areas

Industry/Entity Type

Wedding Photography

Contact Information for Business Card

address: 57 marrow lane, bexton nsw 2041
mobile: 0431872056
phone: (02) 9361 2748
info@goldenhourstudio.net.au
www.goldenhourstudio.net.au
facebook:goldenhourbridals
instagram:goldenhourbridals

Font styles to use
Serif
Sans Serif

Requirements
Nice to have
• maybe add my slogan"love captured in light" if the layout looks good
Should not have
• no black color, not good idea for wedding biz card

```html
<!DOCTYPE html>
<html lang="en">
<head>
<meta charset="utf-8">
<title>Golden Hour Photography and Video – Business Card</title>
<link rel="stylesheet" href="https://fonts.googleapis.com/css2?family=Caveat:wght@600&family=Open+Sans:wght@400;600&display=swap">
<style>
  :root {
    --page: #ffffff;
    --card: #ffffff;
    --gold: #d4a21c;
    --gold-deep: #b8860b;
    --gold-band: linear-gradient(90deg, #c9961a, #e8b923 50%, #c08a14);
    --sage: #a4a8a0;
    --ink: #3a3a38;
    --photo-light: #d9d8cf;
    --photo-mid: #8f8e84;
    --photo-dark: #5f5e56;
  }
  * { box-sizing: border-box; margin: 0; padding: 0; }
  html, body { width: 1095px; height: 1200px; overflow: hidden; background: var(--page); }
  body { position: relative; font-family: "Open Sans", Arial, sans-serif; }

  .card {
    position: absolute;
    width: 750px;
    height: 500px;
    background: var(--card);
    box-shadow: 0 6px 22px rgba(60, 60, 50, 0.22);
    overflow: hidden;
  }
  .card--front { left: 70px; top: 45px; }
  .card--back  { left: 275px; top: 640px; }

  /* Front */
  .brand {
    height: 240px;
    display: flex;
    flex-direction: column;
    align-items: center;
    justify-content: center;
    color: var(--gold);
    font-weight: 600;
    text-align: center;
    padding-top: 10px;
  }
  .brand__name { font-size: 60px; line-height: 1; letter-spacing: 1px; }
  .brand__tag { font-size: 17px; letter-spacing: 9px; margin-top: 16px; text-transform: uppercase; }
  .gold-rule { height: 4px; background: var(--gold-band); }
  .hero-photo {
    height: 256px;
    background: radial-gradient(ellipse at 55% 55%, var(--photo-light) 0%, var(--photo-mid) 45%, var(--photo-dark) 100%);
  }

  /* Back */
  .contact {
    height: 251px;
    background: var(--sage);
    color: #fff;
    display: flex;
    flex-direction: column;
    align-items: center;
    padding-top: 85px;
    font-size: 19px;
    line-height: 38px;
    letter-spacing: 1.8px;
  }
  .slogan-band {
    height: 68px;
    border-top: 4px solid var(--gold);
    border-bottom: 4px solid var(--gold);
    display: flex;
    align-items: center;
    justify-content: center;
    font-family: "Caveat", cursive;
    font-size: 32px;
    color: var(--gold-deep);
    letter-spacing: 3px;
  }
  .online {
    height: 181px;
    display: flex;
    flex-direction: column;
    align-items: center;
    padding-top: 60px;
    gap: 10px;
    color: var(--ink);
    font-size: 19px;
    line-height: 30px;
  }
  .social { display: flex; gap: 36px; }
  .social__item { display: flex; align-items: center; gap: 11px; }
  .social__dot { width: 30px; height: 30px; border-radius: 50%; background: var(--gold); }
</style>
</head>
<body>
  <section class="card card--front">
    <div class="brand">
      <div class="brand__name">Golden Hour</div>
      <div class="brand__tag">Photography and Video</div>
    </div>
    <div class="gold-rule"></div>
    <div class="hero-photo" role="img" aria-label="Black and white night photograph of a wedding party standing on a lamplit park path"></div>
  </section>

  <section class="card card--back">
    <div class="contact">
      <p>57 Marrow Lane, Bexton NSW</p>
      <p>m 0431872056 &nbsp;I&nbsp; p (02) 9361 2748</p>
      <p>e info@goldenhourstudio.net.au</p>
    </div>
    <div class="slogan-band">love captured in light</div>
    <div class="online">
      <div class="social">
        <span class="social__item"><span class="social__dot"></span>goldenhourbridals</span>
        <span class="social__item"><span class="social__dot"></span>goldenhourbridals</span>
      </div>
      <p>www.goldenhourstudio.net.au</p>
    </div>
  </section>
</body>
</html>
```